Shopping Bag Design for Modest Fashion Label

Design a shopping bag for a trendy ladies modest fashion brand. We sell stylish modern modest fashion wear to ladies of all ages. Our brand is about pretty florals and embroidery. Everything pretty and posh. The bag measurements are included in the attachment. Attached is a random sample piece which bear no resemblance to what we have in mind . It is just a mock up. We like pastels colours and the soft yet modern look. Thank you

Target Market(s)

Trendy Ladies looking for modest wear age between 20-60

Industry/Entity Type

fashion

Colors
0054AA
0677BA
7BADD7
CADEEF
E8F1F8

Requirements
Must have
• my logo - NorisaVelle attached in the brief
Should not have
• Animals prints

```html
<!DOCTYPE html>
<html lang="en">
<head>
<meta charset="utf-8">
<title>NorisaVelle Shopping Bag</title>
<link rel="stylesheet" href="https://fonts.googleapis.com/css2?family=Montserrat:wght@500&display=swap">
<style>
  :root {
    --paper: #ffffff;
    --ink: #0a0a0a;
    --bloom-rose: #d9485f;
    --bloom-peach: #f4a877;
    --bloom-coral: #e8734f;
    --leaf-slate: #5b7f9c;
    --leaf-mist: #a9bccb;
  }
  html, body {
    margin: 0;
    padding: 0;
    width: 1200px;
    height: 929px;
    overflow: hidden;
    background: var(--paper);
  }
  .bag-artwork {
    display: block;
    width: 1200px;
    height: 929px;
  }
  .bag-outline {
    fill: none;
    stroke: var(--ink);
    stroke-width: 3;
  }
  .brand-name {
    font-family: "Montserrat", sans-serif;
    font-weight: 500;
    font-size: 92px;
    fill: var(--ink);
  }
</style>
</head>
<body>
<svg class="bag-artwork" viewBox="0 0 1200 929" xmlns="http://www.w3.org/2000/svg">
  <defs>
    <clipPath id="bag-shape">
      <path d="M80 57 H1125 V540 C1125 720 1010 870 804 870 H396 C190 870 80 720 80 540 Z"/>
    </clipPath>
    <linearGradient id="floral-top" x1="0" y1="0" x2="1" y2="0">
      <stop offset="0" stop-color="var(--bloom-rose)"/>
      <stop offset="0.2" stop-color="var(--leaf-slate)"/>
      <stop offset="0.35" stop-color="var(--bloom-coral)"/>
      <stop offset="0.5" stop-color="var(--leaf-mist)"/>
      <stop offset="0.65" stop-color="var(--bloom-peach)"/>
      <stop offset="0.8" stop-color="var(--bloom-rose)"/>
      <stop offset="1" stop-color="var(--bloom-coral)"/>
    </linearGradient>
    <linearGradient id="floral-bottom" x1="0" y1="0" x2="1" y2="0">
      <stop offset="0" stop-color="var(--bloom-peach)"/>
      <stop offset="0.2" stop-color="var(--bloom-rose)"/>
      <stop offset="0.4" stop-color="var(--bloom-peach)"/>
      <stop offset="0.55" stop-color="var(--leaf-slate)"/>
      <stop offset="0.75" stop-color="var(--bloom-coral)"/>
      <stop offset="1" stop-color="var(--leaf-mist)"/>
    </linearGradient>
    <linearGradient id="fade-down" x1="0" y1="0" x2="0" y2="1">
      <stop offset="0" stop-color="#fff" stop-opacity="0"/>
      <stop offset="0.7" stop-color="#fff" stop-opacity="0.35"/>
      <stop offset="1" stop-color="#fff" stop-opacity="1"/>
    </linearGradient>
    <linearGradient id="fade-up" x1="0" y1="1" x2="0" y2="0">
      <stop offset="0" stop-color="#fff" stop-opacity="0"/>
      <stop offset="0.7" stop-color="#fff" stop-opacity="0.35"/>
      <stop offset="1" stop-color="#fff" stop-opacity="1"/>
    </linearGradient>
  </defs>

  <g class="bag-front" clip-path="url(#bag-shape)">
    <g class="floral-border floral-border--top" role="img" aria-label="Watercolour border of pink, coral and peach flowers with slate-blue leaves and berry sprigs">
      <rect x="80" y="57" width="1045" height="265" fill="url(#floral-top)" opacity="0.75"/>
      <rect x="80" y="57" width="1045" height="265" fill="url(#fade-down)"/>
    </g>
    <g class="floral-border floral-border--bottom" role="img" aria-label="Watercolour border of pink, coral and peach flowers with slate-blue leaves and berry sprigs">
      <rect x="80" y="594" width="1045" height="276" fill="url(#floral-bottom)" opacity="0.75"/>
      <rect x="80" y="594" width="1045" height="276" fill="url(#fade-up)"/>
    </g>
  </g>

  <path class="bag-outline" d="M80 57 H1125 V540 C1125 720 1010 870 804 870 H396 C190 870 80 720 80 540 Z"/>

  <text class="brand-name" x="193" y="497" textLength="820" lengthAdjust="spacing">NorisaVelle</text>
</svg>
</body>
</html>
```